Web Design Project

We need a website for a new public relations firm offering PR, advertising, media buying, design and social media. Target clients are professional service firms such as lawyers or CPAs. Looks should be clean and look expensive.

Target Market(s)

Professional service firms. Think business to business companies like consultancy firms.

Industry/Entity Type

Professional Service

Colors

Designer to choose colors to be used in the design.

Requirements
Must have
• Site pages for the purpose of design will include Home, Services, Experience, Bios and Contact Us

```html
<!DOCTYPE html>
<html lang="en">
<head>
<meta charset="utf-8">
<title>Corvell — Marketing, PR, Advertising</title>
<link rel="stylesheet" href="https://fonts.googleapis.com/css2?family=Quicksand:wght@400;500&family=Abel&display=swap">
<style>
  :root {
    --white: #ffffff;
    --ink: #6f6f6f;
    --ink-soft: #9a9a9a;
    --ink-faint: #b8b8b8;
    --line: #dddddd;
    --chip: #ebebeb;
    --band: #ececec;
    --icon: #8a8a8a;
    --field-border: #cfcfcf;
    --hero-dark: #3c4347;
    --hero-mid: #70787c;
    --hero-light: #a7adb0;
  }
  * { box-sizing: border-box; margin: 0; padding: 0; }
  html, body { width: 881px; height: 1200px; overflow: hidden; background: var(--white); }
  body { position: relative; font-family: "Quicksand", sans-serif; color: var(--ink); }
  .abs { position: absolute; }

  /* Header */
  .site-header { position: absolute; left: 0; top: 0; width: 881px; height: 64px; background: var(--white); }
  .brand { position: absolute; left: 87px; top: 18px; font-size: 26px; font-weight: 500; letter-spacing: 2px; color: var(--ink); }
  .main-nav a { position: absolute; top: 16px; height: 31px; line-height: 31px; font-size: 10px; color: var(--ink-soft); text-decoration: none; text-align: center; }
  .main-nav a.is-active { background: var(--chip); border-radius: 3px; }

  /* Hero */
  .hero { position: absolute; left: 0; top: 64px; width: 881px; height: 375px;
    background: linear-gradient(115deg, var(--hero-mid) 0%, var(--hero-dark) 35%, var(--hero-light) 55%, var(--hero-dark) 80%, var(--hero-mid) 100%); }
  .hero-title { position: absolute; left: 233px; top: 160px; width: 416px; height: 53px; border: 3px solid var(--white);
    background: rgba(40,44,47,0.55); color: var(--white); font-family: "Abel", sans-serif; font-size: 24px; text-align: center; line-height: 47px; }
  .hero-arrow { position: absolute; top: 173px; width: 19px; height: 27px; background: var(--white); color: var(--ink); font-size: 10px; text-align: center; line-height: 27px; }

  /* Features */
  .feature { position: absolute; top: 472px; width: 260px; text-align: center; }
  .feature-icon { width: 64px; height: 64px; margin: 0 auto; border-radius: 50%; background: var(--icon); display: flex; align-items: center; justify-content: center; }
  .feature-title { margin-top: 18px; font-size: 14px; letter-spacing: 1.5px; color: var(--ink-soft); font-weight: 400; }
  .feature-text { margin-top: 18px; font-size: 10px; line-height: 12.5px; color: var(--ink-faint); }
  .button { display: inline-block; background: var(--chip); border-radius: 3px; font-size: 10px; color: var(--ink-soft); text-align: center; }
  .feature .button { margin-top: 36px; width: 109px; height: 28px; line-height: 28px; }
  .feature-divider { position: absolute; top: 480px; width: 1px; height: 187px; background: var(--line); }

  /* Info band */
  .info-band { position: absolute; left: 0; top: 707px; width: 881px; height: 250px; background: var(--band); }
  .section-head { position: absolute; display: flex; align-items: center; gap: 8px; font-size: 14px; letter-spacing: 1px; color: var(--ink-soft); }
  .section-icon { width: 30px; height: 30px; border-radius: 50%; background: var(--icon); display: flex; align-items: center; justify-content: center; }
  .map-area { position: absolute; left: 83px; top: 757px; width: 342px; height: 183px; background: linear-gradient(135deg, #e7e3d6, #d9dfc9 60%, #e9e4d3); }
  .contact-form label { position: absolute; left: 453px; font-size: 9.5px; color: var(--ink); }
  .field { position: absolute; left: 453px; width: 347px; border: 1px solid var(--field-border); background: var(--band); font-size: 9px; font-style: italic; color: var(--ink-faint); padding: 3px 4px; }
  .send { position: absolute; left: 716px; top: 918px; width: 84px; height: 22px; line-height: 20px; border: 1px solid #dcdcdc; background: var(--band); font-size: 10px; color: var(--ink-soft); text-align: center; }

  /* Clients */
  .clients-head { position: absolute; left: 83px; top: 985px; width: 717px; display: flex; align-items: center; gap: 18px; font-size: 13px; letter-spacing: 1.5px; color: var(--ink-faint); }
  .clients-head::before, .clients-head::after { content: ""; flex: 1; height: 1px; background: var(--line); }
  .client-grid { position: absolute; left: 83px; top: 1024px; width: 717px; display: grid; grid-template-columns: repeat(5, 120px); column-gap: 29.25px; row-gap: 16px; }
  .client { height: 28px; line-height: 28px; background: var(--chip); border-radius: 3px; font-size: 9.5px; color: var(--ink-faint); text-align: center; }

  /* Footer */
  .footer-rule { position: absolute; left: 0; top: 1107px; width: 881px; height: 3px; background: var(--line); }
  .footer-links a { position: absolute; font-size: 9.5px; color: var(--ink-soft); text-decoration: none; }
  .footer-brand { position: absolute; left: 0; width: 881px; top: 1127px; text-align: center; font-size: 24px; font-weight: 500; letter-spacing: 2px; color: var(--ink-soft); }
  .footer-contact { position: absolute; right: 81px; top: 1122px; text-align: right; font-size: 9.5px; line-height: 15.5px; color: var(--ink-soft); font-style: normal; }
  .legal { position: absolute; left: 0; top: 1176px; width: 881px; height: 24px; line-height: 24px; background: var(--band); text-align: center; font-size: 9px; color: var(--ink-soft); }
</style>
</head>
<body>

<header class="site-header">
  <div class="brand">CORVELL</div>
  <nav class="main-nav">
    <a class="is-active" href="#" style="left:447px;width:70px;">Home</a>
    <a href="#" style="left:530px;width:52px;">Services</a>
    <a href="#" style="left:600px;width:60px;">Experience</a>
    <a href="#" style="left:682px;width:42px;">About</a>
    <a href="#" style="left:752px;width:50px;">Contact</a>
  </nav>
</header>

<section class="hero" role="img" aria-label="Photograph of two businessmen in suits shaking hands, seen from above">
  <div class="hero-arrow" style="left:4px;">&lt;</div>
  <h1 class="hero-title">Marketing - PR- Advertising</h1>
  <div class="hero-arrow" style="left:858px;">&gt;</div>
</section>

<section class="features">
  <div class="feature" style="left:47px;">
    <div class="feature-icon">
      <svg width="30" height="24" viewBox="0 0 30 24" fill="#fff">
        <circle cx="15" cy="6" r="4.5"/><path d="M7 22c0-5 3.5-8 8-8s8 3 8 8z"/>
        <circle cx="6" cy="8" r="3.2"/><path d="M0 20c0-4 2.5-6 6-6 1.3 0 2.4.3 3.3.9C7.4 16.5 6.5 18.5 6.3 20z"/>
        <circle cx="24" cy="8" r="3.2"/><path d="M30 20c0-4-2.5-6-6-6-1.3 0-2.4.3-3.3.9 1.9 1.6 2.8 3.6 3 5.1z"/>
      </svg>
    </div>
    <h2 class="feature-title">ABOUT US</h2>
    <p class="feature-text">Lorem ipsum dolor sit amet,<br>consectetur adipiscing elit,<br>sed do eiusmod tempor</p>
    <span class="button">Read More</span>
  </div>
  <div class="feature-divider" style="left:309px;"></div>
  <div class="feature" style="left:311px;">
    <div class="feature-icon">
      <svg width="32" height="22" viewBox="0 0 32 22" fill="#fff">
        <path d="M0 4l6-2 5 9-5 3z"/><path d="M32 4l-6-2-5 9 5 3z"/>
        <path d="M9 5l6-2 5 1 5 1 3 7-8 8c-1 1-2.5 1-3.5 0L9 13z"/>
      </svg>
    </div>
    <h2 class="feature-title">SERVICES</h2>
    <p class="feature-text">Lorem ipsum dolor sit amet,<br>consectetur adipiscing elit,<br>sed do eiusmod tempor</p>
    <span class="button">Read More</span>
  </div>
  <div class="feature-divider" style="left:573px;"></div>
  <div class="feature" style="left:575px;">
    <div class="feature-icon">
      <svg width="32" height="22" viewBox="0 0 32 22" fill="#fff">
        <path d="M0 4l6-2 5 9-5 3z"/><path d="M32 4l-6-2-5 9 5 3z"/>
        <path d="M9 5l6-2 5 1 5 1 3 7-8 8c-1 1-2.5 1-3.5 0L9 13z"/>
      </svg>
    </div>
    <h2 class="feature-title">EXPERIENCE</h2>
    <p class="feature-text">Lorem ipsum dolor sit amet,<br>consectetur adipiscing elit,<br>sed do eiusmod tempor</p>
    <span class="button">Read More</span>
  </div>
</section>

<section class="info-band"></section>

<div class="section-head" style="left:82px;top:720px;">
  <span class="section-icon">
    <svg width="12" height="16" viewBox="0 0 12 16"><path d="M6 0a6 6 0 0 0-6 6c0 4.5 6 10 6 10s6-5.5 6-10a6 6 0 0 0-6-6z" fill="#fff"/><circle cx="6" cy="6" r="2.2" fill="#8a8a8a"/></svg>
  </span>
  LOCATION
</div>
<div class="map-area" role="img" aria-label="Street map showing the office location"></div>

<div class="section-head" style="left:454px;top:720px;">
  <span class="section-icon">
    <svg width="13" height="10" viewBox="0 0 13 10"><rect width="13" height="10" rx="1" fill="#fff"/><path d="M0.5 1l6 4.5 6-4.5" fill="none" stroke="#8a8a8a" stroke-width="1.2"/></svg>
  </span>
  CONTACT US
</div>
<form class="contact-form">
  <label style="top:764px;">Name:</label>
  <div class="field" style="top:777px;height:19px;">Inserir nome</div>
  <label style="top:803px;">Email:</label>
  <div class="field" style="top:816px;height:19px;">Inserir email</div>
  <label style="top:842px;">Mensagem:</label>
  <div class="field" style="top:856px;height:52px;">Insira sua mensagem</div>
  <div class="send">Send</div>
</form>

<section>
  <h2 class="clients-head" style="font-weight:400;">CLIENTS</h2>
  <div class="client-grid">
    <div class="client">Client 1</div><div class="client">Client 2</div><div class="client">Client 3</div><div class="client">Client 4</div><div class="client">Client 5</div>
    <div class="client">Client 6</div><div class="client">Client 7</div><div class="client">Client 8</div><div class="client">Client 9</div><div class="client">Client 10</div>
  </div>
</section>

<footer>
  <div class="footer-rule"></div>
  <nav class="footer-links">
    <a href="#" style="left:83px;top:1122px;">Home</a>
    <a href="#" style="left:83px;top:1137px;">Services</a>
    <a href="#" style="left:83px;top:1153px;">Experience</a>
    <a href="#" style="left:156px;top:1122px;">About</a>
    <a href="#" style="left:156px;top:1137px;">Contact</a>
  </nav>
  <div class="footer-brand">CORVELL</div>
  <address class="footer-contact">Complete Adress Here<br>555.010.2040<br>contact@corvell.com</address>
  <div class="legal">© 2014 Corvell Marketing - PR Advertising. All Rights Reserved.</div>
</footer>

</body>
</html>
```